Quorvane - corporate Business Card

We need a good look and innovative business card for a new start up company based in Los Angeles called "Quorvane". We are in a payment business, including payment card, app, and ewallet. We are expert in online payment and Card not present (CNP) transaction.
We need an innovative, modern business card.

Our logo font is Aero Matics

Target Market(s)

Startup - Bank - Online Payment - Card Manufacturing

Industry/Entity Type

Startup

Contact Information for Business Card

phone: 628 555 0173 - Address: 4270 Marbrook blvd, Dunmere City, CA 91847

Requirements
Must have
• Message: innovative, professional, expert, high tech, trust, online payment expert, security
Nice to have
• no comment
Should not have
• no Comment

```html
<!DOCTYPE html>
<html lang="en">
<head>
<meta charset="utf-8">
<title>Quorvane business card</title>
<link rel="stylesheet" href="https://fonts.googleapis.com/css2?family=Arimo:wght@400;700&display=swap">
<style>
  :root {
    --backdrop: #4a3f3a;
    --card: #141415;
    --red: #d4212f;
    --white: #f2f2f2;
    --silver: #8d8f92;
    --silver-dim: #6f7174;
  }
  * { box-sizing: border-box; margin: 0; padding: 0; }
  html, body {
    width: 1200px; height: 864px; overflow: hidden;
    background: var(--backdrop);
    font-family: "Arimo", Arial, sans-serif;
  }
  .canvas {
    width: 1200px; height: 864px;
    display: flex; flex-direction: column; align-items: center; justify-content: center;
    gap: 56px;
  }
  .card {
    position: relative;
    width: 600px; height: 343px;
    background: var(--card);
    border-radius: 4px;
    box-shadow: 0 14px 30px rgba(0,0,0,.45);
  }
  /* front */
  .front .brand {
    position: absolute; left: 70px; top: 100px;
    display: flex; align-items: center; gap: 16px;
  }
  .front .brand-dot {
    width: 86px; height: 86px; border-radius: 50%;
    background: var(--silver);
  }
  .front .brand-name {
    font-size: 64px; font-weight: 700; color: var(--silver-dim);
    letter-spacing: 1px;
  }
  .front .site {
    position: absolute; left: 74px; top: 232px;
    font-size: 15px; color: var(--silver);
    letter-spacing: 6px;
  }
  /* back */
  .back .brand {
    position: absolute; right: 30px; top: 58px;
    display: flex; align-items: center; gap: 12px;
  }
  .back .brand-dot {
    width: 62px; height: 62px; border-radius: 50%;
    background: var(--red);
  }
  .back .brand-name {
    font-size: 46px; font-weight: 700; color: var(--red);
    letter-spacing: 1px;
  }
  .back .person {
    position: absolute; left: 34px; top: 138px;
  }
  .back .person-name { font-size: 19px; color: var(--red); line-height: 1.1; }
  .back .person-role { font-size: 16px; color: var(--white); line-height: 1.2; }
  .back .rule {
    position: absolute; left: 34px; right: 30px; top: 181px;
    height: 1.5px; background: var(--white);
  }
  .back .contacts {
    position: absolute; left: 34px; top: 192px;
    list-style: none;
  }
  .back .contacts li {
    display: flex; align-items: center; gap: 9px;
    font-size: 14px; color: var(--white); line-height: 23px;
  }
  .back .contacts svg { width: 13px; height: 13px; flex: none; }
  .back .address {
    position: absolute; right: 30px; bottom: 28px;
    font-size: 16px; color: var(--white); line-height: 1.35;
  }
</style>
</head>
<body>
<main class="canvas">
  <section class="card front" aria-label="Card front">
    <div class="brand">
      <span class="brand-dot"></span>
      <span class="brand-name">quorvane</span>
    </div>
    <p class="site">www.quorvane.com</p>
  </section>

  <section class="card back" aria-label="Card back">
    <div class="brand">
      <span class="brand-dot"></span>
      <span class="brand-name">quorvane</span>
    </div>
    <div class="person">
      <p class="person-name">Mara Venn</p>
      <p class="person-role">President</p>
    </div>
    <div class="rule"></div>
    <ul class="contacts">
      <li>
        <svg viewBox="0 0 16 16" aria-hidden="true"><path fill="#d4212f" d="M3 1h3l1.5 4-2 1.3a9 9 0 0 0 4.2 4.2L11 8.5l4 1.5v3a2 2 0 0 1-2 2A13 13 0 0 1 1 3a2 2 0 0 1 2-2z"/></svg>
        628 555 0173
      </li>
      <li>
        <svg viewBox="0 0 16 16" aria-hidden="true"><rect x="1" y="3" width="14" height="10" rx="1" fill="#d4212f"/><path d="M1.5 3.5 8 9l6.5-5.5" fill="none" stroke="#141415" stroke-width="1.4"/></svg>
        mara@quorvane.com
      </li>
      <li>
        <svg viewBox="0 0 16 16" aria-hidden="true"><circle cx="8" cy="8" r="7" fill="#d4212f"/><path d="M1 8h14M8 1c-3 3.5-3 10.5 0 14M8 1c3 3.5 3 10.5 0 14" fill="none" stroke="#141415" stroke-width="1.1"/></svg>
        www.quorvane.com
      </li>
    </ul>
    <p class="address">4270 Marbrook blvd<br>Dunmere City, CA 91847</p>
  </section>
</main>
</body>
</html>
```